Lumen Cove Skincare - Package Design

New Beauty label needing product packaging design. Looking for elegant and stylish design to represent our premium brand.

This project is for 1 label and 1 box design. The winning designer will be assigned another project for the next product in the range. (to be paid as a new project)

This product is for "Dead Sea Mud Mask". Please see the label format and jar attached. Please note there are 2 different jars we are considering (will have a mud inside). Please feel free to choose whichever one suits your design best.

The labels and boxes are to retain the product information, such as size, ingredients etc, but is to be updated to our brand. You can move or display the other information as you wish.

the size of the dead sea mud mask color box is 72*72*85mm (length*width*height)
the size of dead sea mud mask label is 218*58mm (width*height)

Target Market(s)

Women 15 to 65

Requirements
Must have
• Must be elegant and represent our brand which is a premium beauty product.
Should not have
• Dark blue. Dark purple etc. Colours should compliment the logo

```html
<!DOCTYPE html>
<html lang="en">
<head>
<meta charset="UTF-8">
<title>Lumen Cove Skincare – Dead Sea Mud Mask Label</title>
<link rel="stylesheet" href="https://fonts.googleapis.com/css2?family=Barlow:wght@400;500;600&display=swap">
<style>
  :root {
    --page-bg: #ffffff;
    --label-bg: #2d2725;
    --label-edge: #221d1b;
    --aqua: #8fd4cf;
    --gold: #d9b865;
    --gold-light: #f4e2a6;
    --gold-dark: #b8954c;
    --band-ink: #3a2f22;
    --net-ink: #e6e1dc;
  }
  * { margin: 0; padding: 0; box-sizing: border-box; }
  html, body {
    width: 1200px;
    height: 1200px;
    overflow: hidden;
    background: var(--page-bg);
  }
  .canvas {
    position: relative;
    width: 1200px;
    height: 1200px;
    display: flex;
    align-items: center;
    justify-content: center;
  }
  .label {
    width: 620px;
    height: 580px;
    background: linear-gradient(90deg, var(--label-edge) 0%, var(--label-bg) 12%, var(--label-bg) 88%, var(--label-edge) 100%);
    display: flex;
    flex-direction: column;
    align-items: center;
    padding-top: 62px;
    font-family: "Barlow", sans-serif;
  }
  .brand {
    display: flex;
    align-items: center;
    gap: 12px;
    height: 96px;
  }
  .brand-mark {
    width: 22px;
    height: 22px;
    border-radius: 50%;
    background: var(--gold);
  }
  .brand-name {
    color: var(--gold);
    font-family: "Barlow", sans-serif;
    font-weight: 500;
    font-size: 30px;
    letter-spacing: 0.5px;
  }
  .product-title {
    margin-top: 26px;
    color: var(--aqua);
    font-weight: 500;
    font-size: 56px;
    letter-spacing: 0.5px;
    line-height: 1;
  }
  .benefit-band {
    margin-top: 28px;
    width: 536px;
    height: 40px;
    background: linear-gradient(90deg, var(--gold-dark) 0%, var(--gold-light) 35%, var(--gold) 70%, var(--gold-dark) 100%);
    display: flex;
    align-items: center;
    justify-content: center;
    color: var(--band-ink);
    font-size: 22px;
    font-weight: 400;
  }
  .claims {
    margin-top: 26px;
    text-align: center;
    color: var(--aqua);
    font-size: 24px;
    line-height: 47px;
  }
  .net-weight {
    margin-top: 42px;
    color: var(--net-ink);
    font-size: 24px;
  }
</style>
</head>
<body>
  <main class="canvas">
    <section class="label">
      <div class="brand">
        <span class="brand-mark"></span>
        <span class="brand-name">Lumen Cove Skincare</span>
      </div>
      <h1 class="product-title">DEAD SEA MUD MASK</h1>
      <div class="benefit-band">Anti Acne | Deep Skin Cleanser | Pore Reducer</div>
      <p class="claims">100%&nbsp; Natural and Organic Ingredients<br>With Vitamins to Promote Youtful Skin</p>
      <p class="net-weight">Net Wt 250g | 8.8 fl oz</p>
    </section>
  </main>
</body>
</html>
```